New IPv6 service needs a Web Design

We're launching a brand new service which is designed to connect the current Internet Protocol (IPv4) to the new Internet Protocol (IPv6).
The logo can be found at http://www.lumaport.example
We're looking for a clean and simple design, nothing super-fancy. There has to be room for some menu items and a place where people can login (so an e-mail and password box and login button, which must be replaced by the username and a logout button when the user is logged in).
We need a place for a rotating billboard (see http://vq.example for an example) or a video.
Designs that incorporate IPv4 - IPv6 elements (images with interconnecting networks, videos doing the same) will be rated higher, although the basic design is still the primary concern.
We need :
- A main page, with the rotating billboard and some other typical main page stuff
- 2 subpages with different formatted content blocks (1 column and 2 column)
This is a very short design contest, since we intend to go live very soon. Decision will be made quickly.
PSD file is sufficient, but it must be easy to slice to HTML/CSS (but we'll do that part ourselves).
Target Market(s)
IT Professionals
Industry/Entity Type
Internet
Look and feel
Each slider illustrates characteristics of the customer's brand and the style your logo design should communicate.

```html
<!DOCTYPE html>
<html lang="en">
<head>
<meta charset="utf-8">
<title>Lumaport – interconnecting networks</title>
<link rel="stylesheet" href="https://fonts.googleapis.com/css2?family=Arimo:wght@400;700&family=Ubuntu:wght@400;700&display=swap">
<style>
  :root {
    --page-bg: #dedede;
    --top-band: #6c6c6c;
    --top-band-dark: #555555;
    --nav-bg: #1d1d1d;
    --header-bg: #ececec;
    --panel: #ffffff;
    --border: #e2e2e2;
    --text: #555555;
    --heading: #111111;
    --muted: #7a7a7a;
    --button: #252b33;
    --footer-bar: #5c5c5c;
    --social: #8a8a8a;
    --brand: #1f5e94;
  }
  * { margin: 0; padding: 0; box-sizing: border-box; }
  html, body { width: 1000px; height: 1200px; overflow: hidden; }
  body {
    position: relative;
    background: var(--page-bg);
    font-family: "Arimo", Arial, sans-serif;
    color: var(--text);
  }
  .top-band {
    position: absolute; left: 0; top: 0; width: 1000px; height: 139px;
    background: linear-gradient(180deg, var(--top-band-dark), var(--top-band));
  }
  .phone {
    position: absolute; right: 122px; top: 12px;
    color: #e4e4e4; font-size: 18px; font-weight: 700; letter-spacing: .5px;
  }
  .site {
    position: absolute; left: 121px; top: 50px; width: 759px; height: 1150px;
    background: var(--panel);
  }
  .main-nav {
    height: 40px; background: var(--nav-bg);
    display: flex; align-items: center; padding-left: 10px;
  }
  .main-nav a {
    color: #fff; text-decoration: none; font-size: 12.5px;
  }
  .main-nav .sep { color: #fff; font-size: 12px; margin: 0 17px; }
  .site-header {
    position: relative; height: 116px; background: var(--header-bg);
    border-bottom: 1px solid #d6d6d6;
  }
  .brand {
    position: absolute; left: 22px; top: 38px;
    display: flex; align-items: center; gap: 10px;
    font-family: "Ubuntu", sans-serif; font-weight: 700; font-size: 40px;
    color: var(--brand);
  }
  .brand .mark { width: 14px; height: 14px; border-radius: 50%; background: var(--brand); }
  .login { position: absolute; right: 12px; top: 18px; width: 240px; }
  .login label {
    display: flex; justify-content: space-between; align-items: center;
    font-size: 12px; color: #888; margin-bottom: 8px;
  }
  .login input {
    width: 168px; height: 24px; border: 1px solid #c8c8c8;
    background: linear-gradient(#d8d8d8, #e6e6e6);
  }
  .login button {
    display: block; margin-left: auto; width: 74px; height: 24px; border: 0;
    background: linear-gradient(#3a3a3a, #111); color: #bbb;
    font-family: inherit; font-weight: 700; font-size: 12px;
  }
  .billboard {
    position: relative; height: 265px;
    background: linear-gradient(180deg, #f9f9f9, #ececec);
  }
  .billboard h2 {
    position: absolute; left: 42px; top: 116px;
    font-family: "Ubuntu", sans-serif; font-weight: 400; font-size: 24px; color: var(--heading);
  }
  .billboard .art {
    position: absolute; left: 360px; top: 45px; width: 380px; height: 215px;
    background: radial-gradient(ellipse at 55% 45%, #c9c9c9, #e6e6e6 60%, rgba(236,236,236,0) 75%);
  }
  .features {
    position: absolute; left: 19px; top: 402px; width: 721px;
    display: flex; justify-content: space-between;
  }
  .feature {
    width: 212px; height: 149px; background: #fff; border: 1px solid var(--border);
    box-shadow: 0 6px 6px -4px rgba(0,0,0,.12);
  }
  .feature h3 {
    display: flex; align-items: center; gap: 20px; margin: 22px 0 0 22px;
    font-size: 18px; font-weight: 700; color: #777;
  }
  .feature p { margin: 25px 4px 0 3px; font-size: 11px; line-height: 13px; color: var(--text); }
  .welcome h2 {
    position: absolute; left: 26px; top: 606px;
    font-family: "Ubuntu", sans-serif; font-weight: 400; font-size: 24px; color: var(--heading);
  }
  .welcome .art {
    position: absolute; left: 30px; top: 670px; width: 240px; height: 150px;
    background: radial-gradient(ellipse at center, #e8e8f0, #f7f7f7 70%, #fff);
  }
  .welcome .copy {
    position: absolute; left: 307px; top: 667px; width: 410px;
    font-size: 12px; line-height: 14.6px; color: var(--text);
  }
  .welcome .copy p + p { margin-top: 14px; }
  .read-more {
    position: absolute; left: 604px; top: 836px; width: 101px; height: 33px;
    background: var(--button); color: #fff; border-radius: 4px;
    font-weight: 700; font-size: 13px; display: flex; align-items: center; justify-content: center;
  }
  .divider {
    position: absolute; left: 0; top: 888px; width: 759px; height: 6px;
    background: radial-gradient(ellipse at center top, rgba(0,0,0,.10), rgba(0,0,0,0) 70%);
  }
  .footer-links {
    position: absolute; top: 926px; left: 25px; display: flex;
  }
  .footer-links ul { list-style: none; width: 151px; }
  .footer-links li { font-size: 11px; color: #444; line-height: 24px; }
  .map {
    position: absolute; left: 475px; top: 911px; width: 238px; height: 196px;
    background: linear-gradient(135deg, #e9e4d2, #f1d56a 40%, #a9c1da 65%, #e9e4d2);
  }
  .footer-bar {
    position: absolute; left: 121px; top: 1162px; width: 759px; height: 38px;
    background: var(--footer-bar);
  }
  .social { position: absolute; left: 6px; top: 7px; display: flex; gap: 3px; }
  .social span { width: 25px; height: 25px; background: var(--social); }
  .copyright { position: absolute; right: 8px; top: 16px; font-size: 11px; color: #e8e8e8; }
</style>
</head>
<body>
  <div class="top-band"></div>
  <div class="phone">1400 55501 234</div>

  <div class="site">
    <nav class="main-nav">
      <a href="#">HOME</a><span class="sep">|</span>
      <a href="#">ABOUT US</a><span class="sep">|</span>
      <a href="#">PRODUCTS</a><span class="sep">|</span>
      <a href="#">SERVICES</a><span class="sep">|</span>
      <a href="#">TRAINING</a><span class="sep">|</span>
      <a href="#">CAREERS</a><span class="sep">|</span>
      <a href="#">PARTNERS</a><span class="sep">|</span>
      <a href="#">CONTACT US</a>
    </nav>

    <header class="site-header">
      <div class="brand"><span class="mark"></span>Lumaport</div>
      <form class="login">
        <label>User name <input type="text"></label>
        <label>Password <input type="password"></label>
        <button type="button">Login</button>
      </form>
    </header>

    <section class="billboard">
      <h2>interconnecting networks</h2>
      <div class="art" role="img" aria-label="Chrome chain links interlocking, symbolising connected networks"></div>
    </section>

    <section class="features">
      <article class="feature">
        <h3>
          <svg width="36" height="36" viewBox="0 0 36 36"><circle cx="18" cy="18" r="17" fill="#8a8a8a"/><path d="M25 12a9 9 0 1 0 1 9" fill="none" stroke="#fff" stroke-width="4"/><path d="M21 9h7v7z" fill="#fff"/></svg>
          Network
        </h3>
        <p>Lorem ipsum dolor sit amet, consectetuer adipiscing elit, sed diam nonummy nibh euismod tincidunt ut laoreet dolore magna aliquam erat volutpat.</p>
      </article>
      <article class="feature">
        <h3>
          <svg width="36" height="36" viewBox="0 0 36 36"><rect x="6" y="6" width="24" height="24" transform="rotate(45 18 18)" fill="#7a7a7a"/><path d="M14 23v-5h7" fill="none" stroke="#fff" stroke-width="3"/><path d="M20 14l5 4-5 4z" fill="#fff"/></svg>
          Reach us
        </h3>
        <p>Lorem ipsum dolor sit amet, consectetuer adipiscing elit, sed diam nonummy nibh euismod tincidunt ut laoreet dolore magna aliquam erat volutpat.</p>
      </article>
      <article class="feature">
        <h3>
          <svg width="36" height="36" viewBox="0 0 36 36"><circle cx="18" cy="18" r="17" fill="#8a8a8a"/><text x="18" y="25" text-anchor="middle" font-family="Arial, sans-serif" font-weight="700" font-size="20" fill="#fff">?</text></svg>
          Support
        </h3>
        <p>Lorem ipsum dolor sit amet, consectetuer adipiscing elit, sed diam nonummy nibh euismod tincidunt ut laoreet dolore magna aliquam erat volutpat.</p>
      </article>
    </section>

    <section class="welcome">
      <h2>Welcome to Lumaport</h2>
      <div class="art" role="img" aria-label="Coloured figures standing on a circular network of linked nodes"></div>
      <div class="copy">
        <p>Lorem ipsum dolor sit amet, consectetuer adipiscing elit, sed diam nonummy nibh euismod tincidunt ut laoreet dolore magna aliquam erat volutpat. Ut wisi enim ad minim veniam, quis nostrud exerci tation ullamcorper suscipit lobortis nisl ut aliquip ex ea commodo consequat. Duis autem vel eum iriure dolor in hendrerit in vulputate velit esse molestie consequat, vel illum dolore eu feugiat nulla facilisis at vero eros et accumsan et iusto odio dignissim</p>
        <p>qui blandit praesent luptatum zzril delenit augue duis dolore te feugait nulla facilisi. Nam liber tempor cum soluta nobis eleifend option congue nihil imperdiet doming id quod mazim placerat facer possim assum.</p>
      </div>
      <a class="read-more">Read More</a>
    </section>

    <div class="divider"></div>

    <footer>
      <div class="footer-links">
        <ul><li>News &amp; Info</li><li>Corporate Blog</li><li>Events</li><li>News Center</li><li>Press Room</li><li>Publications</li><li>Social Media</li></ul>
        <ul><li>Cable Operators</li><li>Products</li><li>Sales Inquiries</li><li>Services</li><li>Solutions</li><li>Support</li></ul>
        <ul><li>Enterprise Solutions</li><li>Products</li><li>Partners</li><li>Services</li><li>Support</li><li>Sales Inquiries</li></ul>
      </div>
      <div class="map" role="img" aria-label="Street map showing the office location near the harbour"></div>
    </footer>
  </div>

  <div class="footer-bar">
    <div class="social"><span></span><span></span><span></span><span></span></div>
    <div class="copyright">© 2012 | Privacy policy</div>
  </div>
</body>
</html>
```